Redesign website for small print company

Vindaborgprent is a small printing company in Iceland mainly servicing Students, schools, etc. We are also doing all kind of other jobs, like business cards, book printing, brochure printing etc. We are also selling books online.
Our website is: www.vindaborgprent.is
What we are looking for is:
- Web Design (Uncoded - PSD layout only)
- Mobile friendly design, using our current color scheme: Red, green, yellow and light gray.
- Clean simple design
- Simple, light and easy to use.
- More menu Items/drop down
Industry/Entity Type
Digital Printing
Number of Pages Required
5+ page
Requirements
Must have
- Easy navigation
- Designed for mobile
- Current color scheme (see logo)
Nice to have
- Icon based products

```html
<!DOCTYPE html>
<html lang="is">
<head>
<meta charset="utf-8">
<title>Vindaborgprent</title>
<link href="https://fonts.googleapis.com/css2?family=Roboto:wght@300;400;500;700&display=swap" rel="stylesheet">
<style>
:root{
  --red:#e8403a;
  --red-soft:#f06a63;
  --green:#0b6330;
  --yellow:#f2e51c;
  --gray:#f1f1f1;
  --card:#f4f4f4;
  --ink:#222;
  --muted:#666;
  --dark:#231f20;
  --white:#fff;
}
*{box-sizing:border-box;margin:0;padding:0}
html,body{width:1200px;height:3557px;overflow:hidden}
body{position:relative;font-family:'Roboto',Arial,sans-serif;color:var(--ink);background:var(--white)}
.abs{position:absolute}
.btn{position:absolute;background:var(--red);color:var(--white);border-radius:20px;font-size:13px;font-weight:500;display:flex;align-items:center;justify-content:center}

/* header */
.site-header{position:absolute;left:0;top:0;width:1200px;height:142px;background:var(--white)}
.menu-toggle{left:120px;top:66px;width:26px;height:20px;display:flex;flex-direction:column;justify-content:space-between}
.menu-toggle span{height:3px;background:var(--ink);border-radius:2px}
.brand{display:flex;align-items:center;gap:10px;font-weight:700;color:var(--ink)}
.brand .mark{width:30px;height:30px;background:var(--red)}
.header-brand{left:486px;top:62px;font-size:29px}
.header-tools{left:985px;top:68px;display:flex;gap:18px}

/* hero */
.hero{position:absolute;left:0;top:142px;width:1200px;height:605px;background:var(--gray)}
.hero-photo{left:427px;top:71px;width:773px;height:534px;background:linear-gradient(135deg,#e9dccd,#d7b79a 45%,#c9c0b0)}
.hero-title{left:147px;top:190px;font-size:36px;font-weight:300;color:#666;line-height:48px}
.hero-action{position:absolute;top:308px;width:100px;text-align:center;font-size:11px;font-weight:500}
.hero-action .dot{width:86px;height:86px;border-radius:50%;margin:0 auto 12px;display:flex;align-items:center;justify-content:center}

/* search */
.book-search{left:119px;top:674px;width:960px;height:137px;background:var(--red);border-radius:10px}
.book-search h3{position:absolute;top:16px;width:100%;text-align:center;color:var(--white);font-size:17px;font-weight:500}
.field{position:absolute;top:49px;height:55px;background:var(--red-soft);color:var(--white);font-size:13px;padding:0 14px;display:flex;align-items:center;justify-content:space-between}
.search-btn{position:absolute;left:782px;top:49px;width:147px;height:55px;background:var(--green);color:var(--white);font-size:13px;display:flex;align-items:center;justify-content:center}

/* section titles */
.section-title{position:absolute;width:100%;text-align:center;font-size:31px;font-weight:500}

/* products */
.filter-tabs{left:0;top:919px;width:1200px;display:flex;justify-content:center;gap:0;font-size:13px;color:#444}
.filter-tabs span{padding:0 28px;border-left:1px solid #ccc}
.filter-tabs span:first-child{border-left:none}
.product{position:absolute;top:972px;width:223px}
.product .thumb{height:242px;background:var(--card);position:relative}
.product .cover{position:absolute;left:50px;top:30px;width:120px;height:180px}
.product p{text-align:center;font-size:13px;color:#444;margin-top:28px;line-height:18px}
.product b{display:block;text-align:center;font-size:14px;font-weight:500;margin-top:2px}
.shop-now{left:44px;top:112px;width:134px;height:32px}

/* services */
.services{position:absolute;left:0;top:1466px;width:1200px;height:562px;background:var(--green)}
.service{position:absolute;width:170px;text-align:center;color:var(--white);font-size:17px;font-weight:500}
.service svg{display:block;margin:0 auto 10px}
.service.active{background:var(--red);padding-top:18px;height:113px}

/* testimonials & blog */
.panel{position:absolute;background:var(--card)}
.blog-post{position:absolute;left:605px;width:474px;background:var(--card)}
.blog-img{position:absolute;left:9px;top:9px;width:219px;height:202px}
.date-badge{position:absolute;left:0;top:18px;width:34px;height:36px;background:var(--red);color:var(--white);font-size:11px;font-weight:700;text-align:center;line-height:14px;padding-top:4px}
.blog-body{position:absolute;left:244px;top:10px;width:222px;font-size:12px;line-height:16px;color:#333}

/* contact */
.quick-contact{position:absolute;left:0;top:2782px;width:600px;height:432px;background:var(--green)}
.input{position:absolute;background:var(--white);font-size:12px;padding:10px;color:#333}
.map{left:600px;top:2782px;width:600px;height:432px;background:linear-gradient(135deg,#e8eae6,#dfe6de 50%,#f1ece0)}
.address-card{left:704px;top:2918px;width:269px;height:120px;background:var(--white);font-size:12px;line-height:26px;padding:18px 20px;box-shadow:0 2px 6px rgba(0,0,0,.15)}

/* footer */
.site-footer{position:absolute;left:0;top:3214px;width:1200px;height:343px;background:var(--dark);color:var(--white)}
.footer-col h4{font-size:17px;font-weight:500;margin-bottom:14px}
.footer-col li{list-style:none;font-size:12px;line-height:20px}
.footer-bottom{position:absolute;left:0;top:280px;width:1200px;height:63px;border-top:1px solid #444;font-size:12px;font-weight:500}
</style>
</head>
<body>

<header class="site-header">
  <div class="abs menu-toggle"><span></span><span></span><span></span></div>
  <div class="abs brand header-brand"><span class="mark"></span>VINDABORGPRENT</div>
  <div class="abs header-tools">
    <svg width="16" height="16" viewBox="0 0 16 16"><circle cx="7" cy="7" r="5" fill="none" stroke="#222" stroke-width="2"/><path d="M11 11l4 4" stroke="#222" stroke-width="2"/></svg>
    <svg width="16" height="16" viewBox="0 0 16 16"><circle cx="8" cy="5" r="3.5" fill="none" stroke="#222" stroke-width="1.6"/><path d="M2 15c0-4 3-6 6-6s6 2 6 6" fill="none" stroke="#222" stroke-width="1.6"/></svg>
    <svg width="18" height="16" viewBox="0 0 18 16"><path d="M1 2h3l2 8h9l2-6H5" fill="none" stroke="#222" stroke-width="1.6"/><circle cx="7" cy="14" r="1.3" fill="#222"/><circle cx="14" cy="14" r="1.3" fill="#222"/><circle cx="16" cy="2" r="2" fill="var(--red)"/></svg>
  </div>
</header>

<section class="hero">
  <div class="abs hero-photo" role="img" aria-label="Group of smiling students holding books and folders"></div>
  <h1 class="abs hero-title">Engar áhyggjur<br>... þetta reddast</h1>
  <div class="hero-action" style="left:112px"><div class="dot" style="background:var(--red)"><svg width="34" height="28" viewBox="0 0 34 28"><rect x="2" y="7" width="30" height="20" rx="3" fill="#fff"/><rect x="12" y="2" width="10" height="6" fill="none" stroke="#fff" stroke-width="2.5"/></svg></div>SENDA VERK</div>
  <div class="hero-action" style="left:218px"><div class="dot" style="background:var(--yellow)"><svg width="34" height="34" viewBox="0 0 34 34"><circle cx="17" cy="17" r="13" fill="none" stroke="var(--red)" stroke-width="3"/><path d="M8 8l18 18" stroke="var(--red)" stroke-width="3"/></svg></div>HANNA VERK</div>
  <div class="hero-action" style="left:324px"><div class="dot" style="background:var(--green)"><span style="color:#fff;font-size:40px;font-weight:700">?</span></div>FÁ TILBOÐ</div>
</section>

<form class="abs book-search">
  <h3>Find Your Favorite Book</h3>
  <div class="field" style="left:28px;width:240px">Enter Title</div>
  <div class="field" style="left:279px;width:240px">ISBN or Author</div>
  <div class="field" style="left:531px;width:237px">All Products<span>&#8964;</span></div>
  <div class="search-btn">Search</div>
</form>

<h2 class="section-title" style="top:864px">Feature Product</h2>
<nav class="abs filter-tabs"><span>All</span><span>Books 1</span><span>Books 2</span><span>Books 3</span><span>Other</span></nav>
<svg class="abs" style="left:1042px;top:919px" width="40" height="18" viewBox="0 0 40 18"><circle cx="9" cy="9" r="7" fill="none" stroke="#555" stroke-width="1.5"/><path d="M10 5l-4 4 4 4" fill="none" stroke="#555" stroke-width="1.5"/><circle cx="29" cy="9" r="7" fill="var(--red)"/><path d="M28 5l4 4-4 4" fill="none" stroke="#fff" stroke-width="1.5"/></svg>

<div class="product" style="left:121px"><div class="thumb"><div class="cover" role="img" aria-label="Book cover with colourful splash artwork" style="background:linear-gradient(160deg,#fff,#f4d3b8 50%,#a7cbd6)"></div><div class="btn shop-now">Shop Now</div></div><p>The Craft of Academic<br>Writing</p><b>5.450 KR</b></div>
<div class="product" style="left:368px"><div class="thumb"><div class="cover" role="img" aria-label="Brown book cover with yellow panel" style="background:linear-gradient(180deg,#7a4b1a,#c7a53a 60%,#7a4b1a)"></div></div><p>The Craft of Academic<br>Writing</p><b>5.450 KR</b></div>
<div class="product" style="left:614px"><div class="thumb"><div class="cover" role="img" aria-label="White book cover with red stripe" style="background:linear-gradient(180deg,#fafafa,#e8e8e8)"></div></div><p>Language and the Story of<br>Thought</p><b>$810.00</b></div>
<div class="product" style="left:861px"><div class="thumb"><div class="cover" role="img" aria-label="Statistics book cover with pink title" style="background:linear-gradient(180deg,#e6217c 0 22%,#fafafa 22%)"></div></div><p>Tölfræði í<br>hnotskurn</p><b>5.990 KR</b></div>
<div class="btn" style="left:533px;top:1347px;width:134px;height:34px">View More</div>

<section class="services">
  <h2 class="section-title" style="top:46px;color:#fff">Our Service</h2>
  <div class="service" style="left:102px;top:115px"><svg width="52" height="40" viewBox="0 0 52 40"><rect x="2" y="4" width="48" height="32" rx="3" fill="var(--yellow)"/><circle cx="16" cy="18" r="6" fill="var(--green)"/><rect x="27" y="13" width="17" height="3" fill="var(--green)"/><rect x="27" y="20" width="17" height="3" fill="var(--green)"/><rect x="8" y="28" width="36" height="3" fill="var(--green)"/></svg>Business Cards</div>
  <div class="service" style="left:313px;top:115px"><svg width="52" height="40" viewBox="0 0 52 40"><path d="M10 4l14 4v30l-14-4z" fill="var(--yellow)"/><path d="M26 8l16-4v30l-16 4z" fill="var(--yellow)"/></svg>Brochure</div>
  <div class="service" style="left:515px;top:115px"><svg width="52" height="40" viewBox="0 0 52 40"><path d="M6 6l13 4 14-4 13 4v28l-13-4-14 4-13-4z" fill="var(--yellow)"/><path d="M19 10v28M33 6v28" stroke="var(--green)" stroke-width="2"/></svg>Leaflet</div>
  <div class="service" style="left:736px;top:115px"><svg width="52" height="40" viewBox="0 0 52 40"><path d="M8 24l24-18 14 8-24 18z" fill="var(--yellow)"/><path d="M8 24v6l14 8 24-18v-6" fill="none" stroke="var(--yellow)" stroke-width="4"/></svg>Book Printing</div>
  <div class="service" style="left:952px;top:115px"><svg width="52" height="40" viewBox="0 0 52 40"><rect x="10" y="6" width="32" height="32" rx="3" fill="var(--yellow)"/><rect x="14" y="15" width="24" height="19" fill="var(--green)"/><path d="M20 15v19M26 15v19M32 15v19M14 24h24" stroke="var(--yellow)" stroke-width="2"/></svg>Calander</div>

  <div class="service" style="left:313px;top:243px"><svg width="52" height="40" viewBox="0 0 52 40"><rect x="12" y="4" width="28" height="34" fill="var(--yellow)"/><path d="M12 8h-4M12 14h-4M12 20h-4M12 26h-4M12 32h-4" stroke="var(--yellow)" stroke-width="3"/><rect x="18" y="12" width="16" height="3" fill="var(--green)"/></svg>Spiral Bound</div>
  <div class="service" style="left:313px;top:243px;display:none"></div>
  <div class="service" style="left:102px;top:243px"><svg width="52" height="40" viewBox="0 0 52 40"><rect x="12" y="4" width="28" height="34" fill="var(--yellow)"/><rect x="18" y="12" width="16" height="3" fill="var(--green)"/><rect x="18" y="19" width="16" height="3" fill="var(--green)"/></svg>Spiral Bound</div>
  <div class="service active" style="left:517px;top:221px"><svg width="52" height="40" viewBox="0 0 52 40"><path d="M4 8c8-3 16-3 22 2 6-5 14-5 22-2v28c-8-3-16-3-22 2-6-5-14-5-22-2z" fill="none" stroke="#fff" stroke-width="2.5"/><path d="M26 10v28" stroke="#fff" stroke-width="2.5"/></svg>Textbooks</div>
  <div class="service" style="left:736px;top:243px"><svg width="52" height="40" viewBox="0 0 52 40"><rect x="14" y="4" width="24" height="12" fill="var(--yellow)"/><rect x="8" y="16" width="36" height="16" rx="3" fill="var(--yellow)"/><rect x="16" y="28" width="20" height="10" fill="var(--yellow)" stroke="var(--green)" stroke-width="2"/></svg>Photocopying</div>
  <div class="service" style="left:952px;top:243px"><svg width="52" height="40" viewBox="0 0 52 40"><rect x="12" y="4" width="28" height="34" rx="2" fill="var(--yellow)"/><rect x="17" y="9" width="18" height="14" fill="var(--green)"/><rect x="17" y="27" width="18" height="3" fill="var(--green)"/></svg>Poster</div>

  <div class="service" style="left:102px;top:371px"><svg width="52" height="40" viewBox="0 0 52 40"><circle cx="26" cy="20" r="18" fill="var(--yellow)"/><circle cx="26" cy="20" r="6" fill="var(--green)"/></svg>Cd Cover</div>
  <div class="service" style="left:313px;top:371px"><svg width="52" height="40" viewBox="0 0 52 40"><path d="M10 16l16-8 16 8v18l-16 6-16-6z" fill="var(--yellow)"/><path d="M10 16l16 7 16-7M26 23v17" stroke="var(--green)" stroke-width="2" fill="none"/></svg>Packaging</div>
  <div class="service" style="left:515px;top:371px"><svg width="52" height="40" viewBox="0 0 52 40"><rect x="12" y="2" width="28" height="36" rx="2" fill="var(--yellow)"/><circle cx="26" cy="12" r="4" fill="var(--green)"/><rect x="18" y="20" width="16" height="3" fill="var(--green)"/><rect x="18" y="27" width="16" height="3" fill="var(--green)"/></svg>Resume</div>
  <div class="service" style="left:736px;top:371px"><svg width="52" height="40" viewBox="0 0 52 40"><rect x="8" y="4" width="36" height="34" rx="2" fill="var(--yellow)"/><rect x="13" y="9" width="26" height="5" fill="var(--green)"/><rect x="13" y="18" width="12" height="10" fill="var(--green)"/><path d="M28 19h11M28 24h11M13 32h26" stroke="var(--green)" stroke-width="2"/></svg>Newspaper Ads</div>
  <div class="service" style="left:952px;top:371px"><svg width="52" height="40" viewBox="0 0 52 40"><path d="M8 34l20-30h16l-20 30z" fill="var(--yellow)"/><path d="M8 34h16l2 4H10z" fill="var(--yellow)"/></svg>Magazine</div>
  <div class="btn" style="left:533px;top:481px;width:134px;height:34px">View More</div>
</section>

<h2 class="abs" style="left:121px;top:2110px;width:463px;text-align:center;font-size:27px;font-weight:500">Testimonials</h2>
<p class="abs" style="left:121px;top:2150px;width:463px;text-align:center;font-size:13px">Lorem Ipsum is simply dummy text.</p>
<h2 class="abs" style="left:700px;top:2110px;width:300px;text-align:center;font-size:27px;font-weight:500">Blogs</h2>
<p class="abs" style="left:700px;top:2150px;width:300px;text-align:center;font-size:13px;color:#888">Lorem Ipsum is simply dummy text.</p>
<svg class="abs" style="left:1025px;top:2122px" width="54" height="24" viewBox="0 0 54 24"><circle cx="12" cy="12" r="10" fill="var(--red)"/><path d="M14 7l-5 5 5 5" fill="none" stroke="#fff" stroke-width="2"/><circle cx="40" cy="12" r="9" fill="none" stroke="#333" stroke-width="2"/><path d="M38 7l5 5-5 5" fill="none" stroke="#333" stroke-width="2"/></svg>

<article class="panel" style="left:121px;top:2192px;width:463px;height:443px">
  <div class="abs" role="img" aria-label="Portrait of the reviewer" style="left:184px;top:28px;width:95px;height:95px;border-radius:50%;background:linear-gradient(180deg,#eee,#d9a58a)"></div>
  <h4 class="abs" style="top:150px;width:100%;text-align:center;font-size:17px;font-weight:500">Lena Hart</h4>
  <p class="abs" style="top:175px;width:100%;text-align:center;font-size:13px;color:var(--green)">Creative Director</p>
  <span class="abs" style="left:100px;top:200px;font-size:44px;color:#555">&ldquo;</span>
  <p class="abs" style="left:110px;top:218px;width:243px;text-align:center;font-size:13px;line-height:18px;color:#444">Lorem Ipsum is simply dummy text of the printing and typesetting Lorem Ipsum industry.</p>
  <span class="abs" style="left:330px;top:250px;font-size:44px;color:#555">&rdquo;</span>
  <p class="abs" style="top:282px;width:100%;text-align:center;font-size:13px;color:#444">Read More.. &#9678;</p>
  <p class="abs" style="top:310px;width:100%;text-align:center;font-size:20px;color:#f4b400;letter-spacing:2px">&#9733;&#9733;&#9733;&#9733;&#9733;</p>
  <svg class="abs" style="left:206px;top:343px" width="50" height="8"><circle cx="5" cy="4" r="3.5" fill="var(--green)"/><circle cx="20" cy="4" r="3.5" fill="#bbb"/><circle cx="35" cy="4" r="3.5" fill="#bbb"/></svg>
</article>

<article class="blog-post" style="top:2192px;height:223px">
  <div class="blog-img" role="img" aria-label="Close-up of printer ink cartridges" style="background:linear-gradient(135deg,#2b2b2b,#5b5b5b 50%,#1c1c1c)"></div>
  <div class="date-badge" style="left:9px">01<br>Oct</div>
  <div class="blog-body">
    <div style="display:flex;justify-content:space-between"><b style="font-weight:500">Blog Post Title</b></div>
    <div style="display:flex;justify-content:space-between;margin:4px 0 8px"><span>&#9719; 05 Oct, 2018</span><span>&#9711; 20</span></div>
    <p>Lorem Ipsum is simply dummy text of the And printing matter and type setting industry.</p>
    <p style="margin-top:2px">Lorem Ipsum is simply dummy text of the And printing matter and type setting industry.</p>
    <p style="margin-top:8px">Read More.. &#9678;</p>
  </div>
</article>
<article class="blog-post" style="top:2429px;height:206px">
  <div class="blog-img" role="img" aria-label="Printing press with red light" style="height:188px;background:linear-gradient(135deg,#3a1010,#b3262a 50%,#2a2a2a)"></div>
  <div class="date-badge" style="left:9px">01<br>Oct</div>
  <div class="blog-body">
    <b style="font-weight:500">Blog Post Title</b>
    <div style="display:flex;justify-content:space-between;margin:4px 0 8px"><span>&#9719; 05 Oct, 2018</span><span>&#9711; 20</span></div>
    <p>Lorem Ipsum is simply dummy text of the And printing matter and type setting industry.</p>
    <p style="margin-top:2px">Lorem Ipsum is simply dummy text of the And printing matter and type setting industry.</p>
    <p style="margin-top:8px">Read More.. &#9678;</p>
  </div>
</article>
<div class="btn" style="left:274px;top:2675px;width:134px;height:34px">View More</div>
<div class="btn" style="left:795px;top:2675px;width:134px;height:34px">View More</div>

<section class="quick-contact">
  <h2 class="abs" style="left:119px;top:78px;color:#fff;font-size:31px;font-weight:500">Quick Contact</h2>
  <div class="input" style="left:121px;top:129px;width:204px;height:38px">First Name</div>
  <div class="input" style="left:337px;top:129px;width:204px;height:38px">Last Name</div>
  <div class="input" style="left:121px;top:176px;width:204px;height:38px">Email</div>
  <div class="input" style="left:337px;top:176px;width:204px;height:38px">Phone</div>
  <div class="input" style="left:121px;top:224px;width:420px;height:99px">Message</div>
  <div class="btn" style="left:121px;top:337px;width:166px;height:38px;background:#fff;color:#222">View All</div>
</section>
<div class="abs map" role="img" aria-label="Street map of the shop's neighbourhood"></div>
<svg class="abs" style="left:693px;top:2862px" width="34" height="48" viewBox="0 0 34 48"><path d="M17 0C8 0 1 7 1 16c0 12 16 32 16 32s16-20 16-32C33 7 26 0 17 0z" fill="#e03a2f"/><circle cx="17" cy="16" r="6" fill="#8c1a14"/></svg>
<div class="abs address-card">48 Harbour Lane, Northfield<br>Zip :1234<br>+123 456 7890</div>

<footer class="site-footer">
  <div class="abs brand" style="left:119px;top:86px;font-size:22px;color:#fff"><span class="mark"></span>VINDABORGPRENT</div>
  <p class="abs" style="left:119px;top:140px;width:200px;font-size:13px;line-height:17px">Lorem Ipsum is simply dummy text of the printing and typese tting industry. &#9432;</p>
  <div class="abs" style="left:119px;top:206px;display:flex;gap:5px">
    <span style="width:44px;height:28px;background:#fff;border-radius:2px"></span><span style="width:44px;height:28px;background:#fff;border-radius:2px"></span><span style="width:44px;height:28px;background:#fff;border-radius:2px"></span><span style="width:44px;height:28px;background:#fff;border-radius:2px"></span><span style="width:44px;height:28px;background:#fff;border-radius:2px"></span>
  </div>
  <div class="abs footer-col" style="left:407px;top:78px"><h4>Quick Link</h4><ul style="padding-left:16px"><li>&bull; Home</li><li>&bull; About us</li><li>&bull; Services</li><li>&bull; Blogs</li><li>&bull; Testimonials</li><li>&bull; Contact us</li></ul></div>
  <div class="abs footer-col" style="left:576px;top:78px"><h4>Quick Contact</h4>
    <ul style="font-size:13px"><li style="padding-left:32px;font-size:13px;line-height:22px;position:relative"><span style="position:absolute;left:0">&#9906;</span>48 Harbour Lane<br>Northfield, USA<br>Zip :1234</li>
    <li style="padding-left:32px;font-size:13px;line-height:28px;position:relative"><span style="position:absolute;left:0">&#9742;</span>+123 456 7890</li>
    <li style="padding-left:32px;font-size:13px;line-height:28px;position:relative"><span style="position:absolute;left:0">&#9993;</span>info@vindaborgprent.com</li></ul></div>
  <div class="abs footer-col" style="left:847px;top:78px"><h4>Subscribe</h4><p style="font-size:11px;font-weight:500">Subscribe For Our Newsletter</p></div>
  <div class="abs" style="left:847px;top:142px;width:228px;height:36px;background:#fff;border-radius:18px;font-size:11px;color:#333;display:flex;align-items:center;padding-left:16px">Email Address</div>
  <div class="btn" style="left:1001px;top:142px;width:74px;height:36px;font-size:11px">Subscribe</div>
  <div class="abs" style="left:847px;top:204px;display:flex;gap:9px"><span style="width:24px;height:24px;border-radius:50%;background:#fff"></span><span style="width:24px;height:24px;border-radius:50%;background:#fff"></span><span style="width:24px;height:24px;border-radius:50%;background:#fff"></span><span style="width:24px;height:24px;border-radius:50%;background:#fff"></span></div>
  <div class="footer-bottom">
    <span class="abs" style="left:119px;top:24px">CopyRight &copy; 2018 Vindaborgprent. All Right Reserve</span>
    <span class="abs" style="left:828px;top:24px">Privacy Policy - Terms &amp; Conditions</span>
  </div>
</footer>

</body>
</html>
```